Corvintal Real Estate Business Card

hello, we are a real estate company located in Los Angeles, california. we are a boutique, small company but we like a big corportate look. a simple, sleek, modern and progressive look. we would like the option of having a design that could include the real estate agents personal photo and also a design if the realtor desides not to have a photo. We also would like a hotizontal design.

Corvintal Properties
3817 N Halloway
West Hollywood, CA 90046
www.CorvintalRE.example

Glen Parrish
Broker
BRE # 04829175
(310) 555-0148
glen@corvintalre.example

Industry/Entity Type

Real Estate

```html
<!DOCTYPE html>
<html lang="en">
<head>
<meta charset="utf-8">
<title>Corvintal Real Estate Business Card</title>
<link href="https://fonts.googleapis.com/css2?family=Arimo:wght@400;700&display=swap" rel="stylesheet">
<style>
  :root {
    --backdrop: #111111;
    --paper: #ffffff;
    --navy: #164a89;
    --sky: #2aaae2;
    --text-light: #ffffff;
  }
  * { margin: 0; padding: 0; box-sizing: border-box; }
  html, body {
    width: 1200px; height: 1082px; overflow: hidden;
    background: var(--backdrop);
    font-family: "Arimo", Arial, sans-serif;
  }
  .stage { position: relative; width: 1200px; height: 1082px; }
  .card {
    position: absolute; top: 214px;
    width: 379px; height: 659px;
    background: var(--paper);
    overflow: hidden;
  }
  .card--first { left: 243px; }
  .card--second { left: 636px; }

  .portrait-frame {
    position: absolute; left: 119px; top: 0;
    width: 140px; height: 211px;
    background: var(--paper);
    box-shadow: 0 2px 5px rgba(0,0,0,0.35);
  }
  .portrait-frame__band {
    position: absolute; left: 3px; top: 0; width: 134px; height: 35px;
    background: var(--navy);
  }
  .portrait-frame__photo {
    position: absolute; left: 3px; top: 35px; width: 134px; height: 173px;
    background: linear-gradient(180deg, #b7b49a 0%, #8d8468 45%, #3b3530 75%, #24211f 100%);
  }

  .brand {
    position: absolute; left: 0; top: 262px; width: 100%;
    display: flex; justify-content: center; align-items: center; gap: 12px;
  }
  .brand__mark { width: 30px; height: 30px; background: var(--navy); }
  .brand__name {
    font-size: 44px; font-weight: 400; color: var(--navy);
    letter-spacing: -0.5px; line-height: 1;
  }

  .info-band {
    position: absolute; left: 0; top: 361px; width: 100%; height: 298px;
    background: var(--navy);
  }
  .info-band__accent {
    position: absolute; left: 0; top: 0; width: 54px; height: 100%;
    background: var(--sky);
  }
  .info-band__divider {
    position: absolute; left: 54px; top: 0; width: 4px; height: 100%;
    background: var(--paper);
  }
  .contact {
    position: absolute; left: 74px; top: 31px;
    color: var(--text-light); font-size: 15px; line-height: 19px;
  }
  .contact__name { font-size: 21px; font-weight: 700; line-height: 26px; }
  .contact__group { margin-top: 17px; }
  .contact__group--first { margin-top: 0; }
</style>
</head>
<body>
<div class="stage">

  <article class="card card--first">
    <div class="portrait-frame">
      <div class="portrait-frame__band"></div>
      <div class="portrait-frame__photo" role="img" aria-label="Portrait photo of the broker"></div>
    </div>
    <div class="brand">
      <span class="brand__mark"></span>
      <span class="brand__name">Corvintal</span>
    </div>
    <section class="info-band">
      <div class="info-band__accent"></div>
      <div class="info-band__divider"></div>
      <div class="contact">
        <div class="contact__group contact__group--first">
          <div class="contact__name">GLEN PARRISH</div>
          <div>Broker</div>
          <div>BRE # 04829175</div>
        </div>
        <div class="contact__group">
          <div>Corvintal Properties</div>
          <div>3817 N Halloway</div>
          <div>West Hollywood, CA 90046</div>
        </div>
        <div class="contact__group">
          <div>(310) 555-0148</div>
          <div>glen@corvintalre.example</div>
          <div>www.CorvintalRE.example</div>
        </div>
      </div>
    </section>
  </article>

  <article class="card card--second">
    <div class="portrait-frame">
      <div class="portrait-frame__band"></div>
      <div class="portrait-frame__photo" role="img" aria-label="Portrait photo of the broker"></div>
    </div>
    <div class="brand">
      <span class="brand__mark"></span>
      <span class="brand__name">Corvintal</span>
    </div>
    <section class="info-band">
      <div class="info-band__accent"></div>
      <div class="info-band__divider"></div>
      <div class="contact">
        <div class="contact__group contact__group--first">
          <div class="contact__name">GLEN PARRISH</div>
          <div>Broker</div>
          <div>BRE # 04829175</div>
        </div>
        <div class="contact__group">
          <div>Corvintal Properties</div>
          <div>3817 N Halloway</div>
          <div>West Hollywood, CA 90046</div>
        </div>
        <div class="contact__group">
          <div>(310) 555-0148</div>
          <div>glen@corvintalre.example</div>
          <div>www.CorvintalRE.example</div>
        </div>
      </div>
    </section>
  </article>

</div>
</body>
</html>
```